Storm Restoration Contractor needs a professional business card design

Looking for a professional business card design. Not looking for your cheapo MS Word standard ones that are readily available. Dont want it to be cookie cutter look like ones readily available online. We just recently changed our logo and want to freshen up all our documents. Our company handles restoring a property back to a pre-loss condition after a storm damages it. For example, wind, hail, flood, fire losses.

Target Market(s)

Property Owners, Homeowners, Property Owners, Commercial Property Owners, Property Management Companies, Hail and Wind Damaged Properties

Industry/Entity Type

Construction Company

Contact Information for Business Card

Brightline Facades
847-555-0193
847-555-0147 fax
www.brightlinefacades.example
info@brightlinefacades.example

Requirements
Must have
• Clean, Professional, fresh look
• Storm Restoration, Roofing, Siding, Windows
Nice to have
• If there is a way to incorporate storms that may be cool.

```html
<!DOCTYPE html>
<html lang="en">
<head>
<meta charset="utf-8">
<title>Brightline Facades — Business Card</title>
<link rel="stylesheet" href="https://fonts.googleapis.com/css2?family=Source+Sans+3:wght@400;600&display=swap">
<style>
  :root {
    --backdrop: #8a9a96;
    --card: #050808;
    --brand-blue: #2b86f0;
    --steel: #4f5356;
    --muted: #7b8084;
    --divider: #3a5f8a;
  }
  * { margin: 0; padding: 0; box-sizing: border-box; }
  html, body {
    width: 980px; height: 1200px; overflow: hidden;
    background: var(--backdrop);
    font-family: "Source Sans 3", sans-serif;
  }
  .canvas { position: relative; width: 980px; height: 1200px; }
  .card { position: absolute; background: var(--card); }
  .card--front { left: 126px; top: 132px; width: 713px; height: 410px; }
  .card--back  { left: 120px; top: 711px; width: 712px; height: 413px; }

  .brand-ring {
    position: absolute;
    border: 14px solid var(--brand-blue);
    border-radius: 50%;
  }
  .card--front .brand-ring { left: 251px; top: 74px; width: 210px; height: 210px; }
  .card--back .brand-ring { left: 106px; top: 126px; width: 142px; height: 142px; border-width: 10px; }

  .brand-name {
    position: absolute;
    color: var(--brand-blue);
    font-weight: 600;
    text-transform: uppercase;
    white-space: nowrap;
    text-align: center;
  }
  .card--front .brand-name { left: 0; right: 0; top: 290px; font-size: 32px; letter-spacing: 3px; }
  .card--back .brand-name { left: 20px; width: 316px; top: 276px; font-size: 22px; letter-spacing: 2px; }

  .services {
    position: absolute; left: 0; right: 0; top: 342px;
    text-align: center; white-space: nowrap;
    font-size: 15px; font-weight: 400; letter-spacing: 2px;
    text-transform: uppercase; color: var(--muted);
  }
  .services span + span::before { content: "•"; margin: 0 10px; color: var(--brand-blue); }

  .divider {
    position: absolute; left: 357px; top: 119px;
    width: 1px; height: 206px; background: var(--divider);
  }
  .company {
    position: absolute; left: 387px; top: 70px;
    font-size: 28px; font-weight: 400; color: var(--brand-blue);
  }
  .contact-list { position: absolute; left: 406px; top: 168px; list-style: none; }
  .contact-item {
    display: flex; align-items: center; gap: 14px;
    height: 43px; font-size: 18px; color: var(--muted);
    white-space: nowrap;
  }
  .contact-item svg { width: 24px; height: 24px; flex: none; }
  .contact-label { color: var(--brand-blue); font-size: 15px; margin-left: 6px; }
</style>
</head>
<body>
<main class="canvas">
  <section class="card card--front" aria-label="Card front">
    <div class="brand-ring"></div>
    <p class="brand-name">Brightline Facades</p>
    <p class="services"><span>Storm Restoration</span><span>Roofing</span><span>Siding</span><span>Windows</span></p>
  </section>

  <section class="card card--back" aria-label="Card back">
    <div class="brand-ring"></div>
    <p class="brand-name">Brightline Facades</p>
    <div class="divider"></div>
    <h1 class="company">Brightline Facades</h1>
    <ul class="contact-list">
      <li class="contact-item">
        <svg viewBox="0 0 24 24" aria-hidden="true"><path fill="#2b86f0" d="M6.6 3.5l2.6 3.4-1.6 2.1c1.1 2.4 3 4.3 5.4 5.4l2.1-1.6 3.4 2.6-1.2 3.1c-7.3-.3-12.9-5.9-13.2-13.2z"/></svg>
        <span>847-555-0193</span>
      </li>
      <li class="contact-item">
        <svg viewBox="0 0 24 24" aria-hidden="true" fill="none" stroke="#2b86f0" stroke-width="1.3"><rect x="6" y="2" width="12" height="10"/><path d="M8 5h8M8 7.5h6"/><path d="M3 11v11h18V11l-9 6z"/></svg>
        <span>847-555-0147<span class="contact-label">fax</span></span>
      </li>
      <li class="contact-item">
        <svg viewBox="0 0 24 24" aria-hidden="true" fill="none" stroke="#2b86f0" stroke-width="1.3"><rect x="6" y="2" width="12" height="10"/><path d="M8 5h8M8 7.5h6"/><path d="M3 11v11h18V11l-9 6z"/></svg>
        <span>info@brightlinefacades.example</span>
      </li>
      <li class="contact-item">
        <svg viewBox="0 0 24 24" aria-hidden="true" fill="none" stroke="#2b86f0" stroke-width="1.3"><circle cx="12" cy="12" r="9.5"/><ellipse cx="12" cy="12" rx="4" ry="9.5"/><path d="M2.5 12h19M4 7h16M4 17h16"/></svg>
        <span>www.brightlinefacades.example</span>
      </li>
    </ul>
  </section>
</main>
</body>
</html>
```